Medical Marihuana Ziplock Bag Mockup Design

We seek skilled and professional designer for medical marihuana ziplock bag packaging design. We need a modern, minimal, clean Design with the name productname: Plorix - Endproduct will be a ziplock bag (see attachment) samples.
Product may but must not contain a cannabis leaf in Design7Logo

Target Market(s)

young audience

Industry/Entity Type

Medical

Logo Text

P L O R X

Font styles to use
Serif
Sans Serif

Colors
9bcb3c
abd037
cadf82
ffc214
fece3e
fee18a
6b449b
886aae
b8a6cd

Requirements
Nice to have
• Can but must not contain a minimal cannabis leaf as abstract sign

```html
<!DOCTYPE html>
<html lang="de">
<head>
<meta charset="utf-8">
<title>Plorix – Medical Marijuana</title>
<link href="https://fonts.googleapis.com/css2?family=Roboto+Slab:wght@300;400;700&display=swap" rel="stylesheet">
<style>
  :root {
    --green-top: #66993f;
    --green-logo: #5f9a3c;
    --pill: #8cc63f;
    --dark: #2c5127;
    --light-green: #8cc63f;
    --field-top: #7cb342;
    --field-bottom: #2d4f27;
    --white: #ffffff;
    --grey: #d9dadd;
  }
  * { margin: 0; padding: 0; box-sizing: border-box; }
  html, body { width: 901px; height: 1200px; overflow: hidden; }
  body { font-family: "Roboto Slab", serif; }
  .bag { position: relative; width: 901px; height: 1200px; overflow: hidden;
    background: linear-gradient(to bottom, var(--white) 0, var(--white) 300px, var(--grey) 451px); }
  .top-band { position: absolute; left: 0; top: 0; width: 100%; height: 52px; background: var(--green-top); }
  .age { position: absolute; right: 24px; top: 76px; font-size: 38px; font-weight: 400; color: var(--green-logo); }
  .brand { position: absolute; left: 0; width: 100%; top: 180px; text-align: center;
    font-size: 150px; font-weight: 300; color: var(--green-logo); line-height: 1; letter-spacing: 4px; }
  .info-band { position: absolute; left: 0; top: 451px; width: 100%; height: 173px; background: var(--dark); }
  .pill { position: absolute; left: 191px; top: 423px; width: 519px; height: 68px; border-radius: 30px;
    background: var(--pill); color: var(--white); font-weight: 700; font-size: 41px;
    display: flex; align-items: center; justify-content: center; box-shadow: 0 4px 6px rgba(0,0,0,.35); }
  .origin { position: absolute; top: 522px; width: 100%; text-align: center; color: var(--white); font-size: 28px; font-weight: 400; }
  .tagline { position: absolute; top: 573px; width: 100%; text-align: center; color: var(--light-green); font-size: 30px; font-weight: 300; }
  .rule { position: absolute; left: 0; top: 627px; width: 100%; height: 5px; background: #a8d45a; }
  .field { position: absolute; left: 0; top: 632px; width: 100%; height: 568px;
    background: linear-gradient(to bottom, var(--field-top), #4e7f35 45%, var(--field-bottom)); }
  .leaf-art { position: absolute; left: 16px; top: 676px; width: 362px; height: 484px;
    background: radial-gradient(ellipse at 50% 55%, rgba(120,175,70,.45), rgba(120,175,70,0) 70%); }
  .divider { position: absolute; left: 376px; top: 660px; width: 2px; height: 377px; background: var(--white); }
  .warning { position: absolute; left: 398px; top: 675px; width: 480px; color: var(--white);
    font-size: 28px; line-height: 38px; font-weight: 400; }
  .weight { position: absolute; left: 52px; top: 1075px; color: var(--white); font-size: 66px; line-height: 1; }
  .weight b { font-weight: 700; }
  .weight span { font-weight: 300; }
  .cross { position: absolute; left: 654px; top: 1071px; }
  .strains { position: absolute; left: 785px; top: 1079px; list-style: none; }
  .strains li { display: flex; align-items: center; height: 29.5px; color: var(--white); font-size: 15px; }
  .strains li::before { content: ""; width: 18px; height: 18px; border: 2px solid #222; background: var(--white); margin-right: 10px; }
</style>
</head>
<body>
<div class="bag">
  <div class="top-band"></div>
  <div class="age">18+</div>
  <div class="brand">Plorix</div>

  <div class="info-band"></div>
  <div class="pill">Medical Marijuana</div>
  <div class="origin">100% SCHWEIZER HANF</div>
  <div class="tagline">Product auf pflanzlicher Basis ohne Tabak</div>
  <div class="rule"></div>

  <div class="field"></div>
  <div class="leaf-art" role="img" aria-label="Faint cannabis leaf illustration"></div>
  <div class="divider"></div>
  <p class="warning">Rauchen fügt ihnen und den Menschen in ihrer Umgebung erheblichen Schaden zu.<br>Fumer nuit Gravement à votre santé et à celle de votre entourage.<br>Il fumo daneggia gravemente te e chi ti sta intorno.</p>

  <div class="weight"><b>10</b><span>g</span></div>
  <svg class="cross" width="96" height="96" viewBox="0 0 96 96" aria-hidden="true">
    <path d="M30 0h36v30h30v36H66v30H30V66H0V30h30z" fill="#5e9a3a"/>
  </svg>
  <ul class="strains">
    <li>INDICA</li>
    <li>SATIVA</li>
    <li>HYBRID</li>
  </ul>
</div>
</body>
</html>
```